We need a new design for our construction website

We need a new website for our wordpress site ferncrestworks.co.nz

It needs to be only a few pages but sleek in design and responsive, beautifully showcasing our images and video. Currently we have
1. home
2. about us
3. contact
We need either a front page that is designed much better to showcase more content, or potentially a projects page which has images from our builds. We don't have a lot of content so the content we do have needs to be maximised by image, rather than project.

Target Market(s)

High end residential construction and renovation projects, people wanting to build a nice home, clients based in Mount Maunganui, Tauranga.

Coding

Font styles to use
Sans Serif

Colors

Designer to choose only greyscale colors for use in the design.

Requirements
Must have
• A sleek design, architectural

```html
<!DOCTYPE html>
<html lang="en">
<head>
<meta charset="utf-8">
<title>Ferncrest — High end residential construction</title>
<link rel="stylesheet" href="https://fonts.googleapis.com/css2?family=Montserrat:wght@400;500;700;800&family=Work+Sans:wght@400;500&display=swap">
<style>
:root{
  --ink:#111;
  --text:#555;
  --muted:#777;
  --btn:#7a7a7a;
  --panel:#efeff0;
  --line:#d6d6d6;
  --white:#fff;
  --sky-top:#cfd1d4;
  --sky-bottom:#e6e7e9;
}
*{margin:0;padding:0;box-sizing:border-box}
html,body{width:1200px;height:3816px;overflow:hidden;background:var(--white)}
body{position:relative;font-family:"Work Sans",Arial,sans-serif;color:var(--ink)}
.abs{position:absolute}
.label{position:absolute;font-family:"Montserrat",Arial,sans-serif;font-size:12.5px;letter-spacing:1px;color:#333;display:flex;align-items:center}
.label::before{content:"";display:inline-block;width:39px;height:1px;background:#333;margin-right:11px}
.h2{position:absolute;font-family:"Montserrat",Arial,sans-serif;font-weight:800;font-size:35px;line-height:47px;letter-spacing:.3px;color:var(--ink)}
.photo{position:absolute}
.btn{position:absolute;width:54px;height:53px;background:var(--btn)}
.btn span{position:absolute;left:20px;top:18px;white-space:nowrap;font-family:"Montserrat",Arial,sans-serif;font-size:13.5px;font-weight:500;color:#111;display:flex;align-items:center;gap:8px}

/* hero */
.hero{position:absolute;left:0;top:0;width:1200px;height:600px;background:linear-gradient(180deg,var(--sky-top),var(--sky-bottom))}
.hero-building{position:absolute;left:300px;top:100px;width:820px;height:500px;background:linear-gradient(115deg,rgba(230,231,233,0) 0%,#9a9c9f 12%,#5e6064 30%,#2f3033 48%,#6f7175 62%,#a9abae 80%,rgba(220,221,223,.2) 100%)}
.brand{position:absolute;left:27px;top:50px;display:flex;align-items:center;gap:14px;font-family:"Montserrat",Arial,sans-serif;font-size:22px;letter-spacing:7px;color:#555}
.brand i{display:block;width:26px;height:26px;border:2px solid #555}
.nav{position:absolute;top:60px;left:865px;font-family:"Montserrat",Arial,sans-serif;font-size:11.5px;letter-spacing:.5px;color:#222}
.nav a{position:absolute;white-space:nowrap;text-decoration:none;color:inherit}
.nav .active{border-top:1.5px solid #222;padding-top:8px;margin-top:-9px}
.social{position:absolute;width:24px;height:24px;border:1.5px solid #333}
.hero-title{position:absolute;left:24px;top:164px;font-family:"Montserrat",Arial,sans-serif;font-weight:800;font-size:49px;line-height:72px;color:#0b0b0b}
.contact-v{position:absolute;left:1126px;top:163px;height:270px;writing-mode:vertical-rl;transform:rotate(180deg);font-family:"Montserrat",Arial,sans-serif;font-size:12px;color:#222;display:flex;align-items:center;gap:10px}
.hero-thumbs{position:absolute;left:753px;top:504px;width:447px;height:96px;background:var(--white)}
.thumb{position:absolute;top:10px;height:76px;background:linear-gradient(180deg,#c9cacc 0%,#e0e0e1 30%,#4c4d50 55%,#8a8b8d 75%,#3a3b3d 100%)}

/* about */
.about-text{position:absolute;left:172px;top:892px;width:416px;font-size:12px;letter-spacing:.35px;line-height:18.8px;color:var(--text);text-align:justify}
.video{position:absolute;left:612px;top:736px;width:415px;height:415px;background:linear-gradient(180deg,#6a6c70 0%,#9a9b9e 18%,#3e3f42 30%,#c9cacc 48%,#f2f2f2 62%,#8d8e90 78%,#6b6c6e 100%)}
.play{position:absolute;left:788px;top:925px;width:60px;height:40px;border-radius:10px;background:#2a2a2a}
.play::after{content:"";position:absolute;left:25px;top:12px;border-left:14px solid #fff;border-top:8px solid transparent;border-bottom:8px solid transparent}

/* services */
.service{position:absolute;left:609px;width:425px}
.service h3{font-family:"Montserrat",Arial,sans-serif;font-weight:800;font-size:24px;line-height:30px;color:var(--ink);margin-bottom:7px}
.service p{font-size:12px;letter-spacing:.3px;line-height:18.7px;color:var(--text)}

/* properties */
.filters{position:absolute;top:1943px;font-family:"Montserrat",Arial,sans-serif;font-size:13px;color:#222}
.filters span{position:absolute;white-space:nowrap}
.property{position:absolute;top:2012px;width:240px;height:373px}
.property h4{position:absolute;left:22px;top:279px;font-family:"Montserrat",Arial,sans-serif;font-weight:800;font-size:15.5px;line-height:22px;color:#fff}
.property small{position:absolute;left:22px;top:344px;font-family:"Montserrat",Arial,sans-serif;font-size:11px;letter-spacing:.5px;color:#ddd;display:flex;align-items:center;gap:10px}

/* testimonials */
.quote{position:absolute;top:2613px;width:416px;height:243px;background:var(--panel)}
.quote .mark{position:absolute;left:8px;top:36px;font-family:"Montserrat",Arial,sans-serif;font-size:28px;font-weight:700;color:#aaa;line-height:1}
.quote p{position:absolute;left:34px;top:40px;width:364px;font-size:12px;letter-spacing:.35px;line-height:18.8px;color:var(--text);text-align:justify}
.quote .avatar{position:absolute;left:35px;top:166px;width:54px;height:54px;border-radius:50%;background:linear-gradient(135deg,#b3b3b3,#4e4e4e)}
.quote .name{position:absolute;left:100px;top:185px;font-family:"Montserrat",Arial,sans-serif;font-size:14px;font-weight:500;color:#333}

/* badges */
.badge{position:absolute;top:2951px;width:271px;height:135px;border:1.5px solid var(--line);background:#fff}
.badge i{position:absolute;display:block;background:#555}

/* news */
.article{position:absolute;top:3280px;width:271px;height:373px}
.article h4{position:absolute;left:16px;top:265px;width:250px;font-family:"Montserrat",Arial,sans-serif;font-weight:800;font-size:16.5px;line-height:25px;color:#fff}
.article small{position:absolute;left:22px;top:334px;font-size:11.5px;color:#eee;word-spacing:2px}
.article small b{font-weight:400;margin-right:24px}

/* footer */
.footer{position:absolute;left:0;top:3730px;width:1200px;height:86px;background:var(--panel)}
.footer .copy{position:absolute;left:175px;top:35px;font-family:"Montserrat",Arial,sans-serif;font-size:11.5px;color:#222}
.footer .links{position:absolute;left:809px;top:35px;font-family:"Montserrat",Arial,sans-serif;font-size:11.5px;color:#222}
</style>
</head>
<body>

<header class="hero">
  <div class="hero-building" role="img" aria-label="Modern glass building with cantilevered floors against a pale sky"></div>
  <div class="brand"><i></i>FERNCREST</div>
  <nav class="nav">
    <a class="active" style="left:0">HOME</a>
    <a style="left:67px">ABOUT</a>
    <a style="left:136px">CONTACT</a>
  </nav>
  <div class="social" style="left:1121px;top:52px"></div>
  <h1 class="hero-title">High end residential<br>construction and<br>renovation</h1>
  <a class="btn" style="left:27px;top:424px"><span>OUR PROJECTS
    <svg width="14" height="8" viewBox="0 0 14 8"><path d="M0 4h12M9 1l3 3-3 3" stroke="#111" stroke-width="1.6" fill="none"/></svg></span></a>
  <div class="contact-v">
    <svg width="12" height="12" viewBox="0 0 12 12" style="transform:rotate(90deg)"><path d="M2 1l2 0 1 3-1.5 1a7 7 0 0 0 3.5 3.5L8 7l3 1v2a1 1 0 0 1-1 1A10 10 0 0 1 1 2a1 1 0 0 1 1-1z" fill="#222"/></svg>
    <span>0271480392</span>
    <svg width="12" height="10" viewBox="0 0 12 10" style="margin-top:8px"><rect x="0.5" y="0.5" width="11" height="9" fill="#222"/><path d="M1 1l5 4 5-4" stroke="#fff" fill="none"/></svg>
    <span>admin@ferncrestworks.co.nz</span>
  </div>
  <div class="hero-thumbs">
    <div class="thumb" style="left:38px;width:111px" role="img" aria-label="Building exterior thumbnail"></div>
    <div class="thumb" style="left:167px;width:111px" role="img" aria-label="Building exterior thumbnail"></div>
    <div class="thumb" style="left:293px;width:102px" role="img" aria-label="Building exterior thumbnail"></div>
  </div>
</header>

<section class="about">
  <div class="label" style="left:172px;top:681px">ABOUT US</div>
  <h2 class="h2" style="left:172px;top:729px">An architectural<br>company based in<br>Tauranga</h2>
  <p class="about-text">Kauri Ridge Homes Ltd T/A Ferncrest was founded in 1985 by Neil Hartley and began trading as Ferncrest in 2017 with sons Sam and Jonah at the helm. With the company's roots previously in solid timber, the team have a special interest in architectural homes, alternative building technologies and sustainable building practices. Ferncrest's team have an exceptional understanding of alternative building materials and are happy to work with your architect or designer to ensure your build is as enjoyable and hassle-free as possible.</p>
  <a class="btn" style="left:173px;top:1102px"><span>READ MORE
    <svg width="14" height="8" viewBox="0 0 14 8"><path d="M0 4h12M9 1l3 3-3 3" stroke="#111" stroke-width="1.6" fill="none"/></svg></span></a>
  <div class="video" role="img" aria-label="Video still of a modern two-storey home with timber fence and lawn"></div>
  <div class="play"></div>
</section>

<section class="services">
  <div class="label" style="left:612px;top:1236px">OUR SERVICES</div>
  <div class="photo" style="left:172px;top:1284px;width:209px;height:267px;background:linear-gradient(180deg,#f0f0f0 0%,#8f8f8f 20%,#e6e6e6 45%,#bdbdbd 70%,#3a3a3a 100%)" role="img" aria-label="Black and white modern house exterior"></div>
  <div class="photo" style="left:393px;top:1339px;width:196px;height:157px;background:linear-gradient(110deg,#5a5a5a 0%,#9c9c9c 35%,#f2f2f2 60%,#b8b8b8 100%)" role="img" aria-label="Black and white curved architectural facade"></div>
  <div class="photo" style="left:173px;top:1606px;width:194px;height:157px;background:linear-gradient(180deg,#2e2e2e 0%,#7a7a7a 25%,#4c4c4c 55%,#9c9c9c 75%,#262626 100%)" role="img" aria-label="Black and white bedroom interior with stone wall"></div>
  <div class="photo" style="left:379px;top:1551px;width:209px;height:267px;background:linear-gradient(180deg,#e4e4e4 0%,#f4f4f4 35%,#b5b5b5 60%,#7a7a7a 80%,#a8a8a8 100%)" role="img" aria-label="Black and white living room with high ceiling"></div>

  <div class="service" style="top:1280px"><h3>Design and Build</h3><p>The Design and Build process streamlines your home construction project ensuring your architect or designer and builder are on the same page from day one meaning you get the dream home you've always wanted.</p></div>
  <div class="service" style="top:1410px"><h3>Renovations &amp; Additions</h3><p>Improving the layout and functionality of your home doesn't mean having to build from scratch, renovations and additions can modernise your home, improve things like energy efficiency and the way that your building "performs."</p></div>
  <div class="service" style="top:1541px"><h3>Project Management</h3><p>We specialise in managing your entire build project. From liaising with your designer, engineers, advising you on the best building materials, sourcing trustworthy subcontractors and scheduling and managing the roll-out of each build stage. We are experienced and have a reputation for on-time, on-budget builds.</p></div>
  <div class="service" style="top:1691px"><h3>Build Smarter</h3><p>We are passionate about building smarter, even better than the building code. When it comes to energy efficiency, a warm and healthy home performs with true efficiency. What do we mean? Comfort, thermally-broken, well designed and the best quality materials to match your project budget.</p></div>
</section>

<section class="properties">
  <div class="label" style="left:27px;top:1943px">OUR PROPERTIES</div>
  <div class="filters"><span style="left:899px">All Properties</span><span style="left:1030px">Exterior</span><span style="left:1121px">Interior</span></div>
  <div class="property" style="left:0;background:linear-gradient(180deg,#e0e0e0 0%,#8a8a8a 30%,#c4c4c4 50%,#4a4a4a 75%,#2a2a2a 100%)" role="img" aria-label="Black and white timber clad house exterior"><h4>Nam libero tempore<br>cum soluta nobis</h4><small>VIEW PROJECT <svg width="14" height="8" viewBox="0 0 14 8"><path d="M0 4h12M9 1l3 3-3 3" stroke="#ddd" stroke-width="1.6" fill="none"/></svg></small></div>
  <div class="property" style="left:240px;background:linear-gradient(180deg,#f2f2f2 0%,#c8c8c8 30%,#7c7c7c 55%,#a0a0a0 70%,#333 100%)" role="img" aria-label="Black and white kitchen interior"><h4>Nam libero tempore<br>cum soluta nobis</h4><small>VIEW PROJECT <svg width="14" height="8" viewBox="0 0 14 8"><path d="M0 4h12M9 1l3 3-3 3" stroke="#ddd" stroke-width="1.6" fill="none"/></svg></small></div>
  <div class="property" style="left:480px;background:linear-gradient(180deg,#ececec 0%,#d8d8d8 35%,#8e8e8e 60%,#5c5c5c 80%,#2e2e2e 100%)" role="img" aria-label="Black and white lounge with chandelier"><h4>Nam libero tempore<br>cum soluta nobis</h4><small>VIEW PROJECT <svg width="14" height="8" viewBox="0 0 14 8"><path d="M0 4h12M9 1l3 3-3 3" stroke="#ddd" stroke-width="1.6" fill="none"/></svg></small></div>
  <div class="property" style="left:720px;background:linear-gradient(160deg,#bcbcbc 0%,#f0f0f0 35%,#6e6e6e 60%,#d0d0d0 75%,#404040 100%)" role="img" aria-label="Black and white angular modern house"><h4>Nam libero tempore<br>cum soluta nobis</h4><small>VIEW PROJECT <svg width="14" height="8" viewBox="0 0 14 8"><path d="M0 4h12M9 1l3 3-3 3" stroke="#ddd" stroke-width="1.6" fill="none"/></svg></small></div>
  <div class="property" style="left:960px;background:linear-gradient(180deg,#1c1c1c 0%,#4a4a4a 20%,#dadada 45%,#f2f2f2 65%,#6a6a6a 85%,#2a2a2a 100%)" role="img" aria-label="Black and white bedroom interior"><h4>Nam libero tempore<br>cum soluta nobis</h4><small>VIEW PROJECT <svg width="14" height="8" viewBox="0 0 14 8"><path d="M0 4h12M9 1l3 3-3 3" stroke="#ddd" stroke-width="1.6" fill="none"/></svg></small></div>
</section>

<section class="testimonials">
  <div class="label" style="left:172px;top:2478px">OUR TESTIMONIALS</div>
  <h2 class="h2" style="left:172px;top:2514px">What People Say About Us</h2>
  <svg class="abs" style="left:990px;top:2580px" width="38" height="10" viewBox="0 0 38 10"><path d="M14 5H2M5 2L2 5l3 3M24 5h12M33 2l3 3-3 3" stroke="#111" stroke-width="1.6" fill="none"/></svg>
  <div class="quote" style="left:172px"><span class="mark">&#8221;</span><p>Our home is the envy of many friends. It holds the warmth incredibly through the winter and is perfectly cool in the summer. The ease of design has made it not only very smart with a modern feel but also with its strong robust construction it feels safe and secure for our young family. We love our home!</p><div class="avatar" role="img" aria-label="Client photo"></div><span class="name">Hannah</span></div>
  <div class="quote" style="left:610px"><span class="mark">&#8221;</span><p>Temporibus autem quibusdam et aut officiis debitis aut rerum necessitatibus saepe eveniet ut et voluptates repudiandae sint et molestiae non recusandae. Itaque earum rerum hic tenetur a sapiente delectus, ut aut reiciendis voluptatibus maiores alias consequatur aut perferendis doloribus asperiores repellat.</p><div class="avatar" style="background:linear-gradient(135deg,#e6e6e6,#8c8c8c)" role="img" aria-label="Client photo"></div><span class="name">Quis autem vel eum</span></div>
</section>

<section class="badges">
  <div class="badge" style="left:172px"><i style="left:105px;top:28px;width:62px;height:62px"></i></div>
  <div class="badge" style="left:465px"><i style="left:100px;top:22px;width:72px;height:72px;border-radius:50%"></i></div>
  <div class="badge" style="left:757px"><i style="left:26px;top:40px;width:56px;height:56px;border-radius:50%"></i><i style="left:96px;top:52px;width:145px;height:30px;background:#888"></i></div>
</section>

<section class="news">
  <div class="label" style="left:172px;top:3159px">NEWS</div>
  <h2 class="h2" style="left:170px;top:3195px">Latest Articles</h2>
  <div class="article" style="left:170px;background:linear-gradient(180deg,#f0f0f0 0%,#9a9a9a 25%,#5a5a5a 50%,#8a8a8a 65%,#222 100%)" role="img" aria-label="Black and white modern house facade"><h4>Excepteur sint occaecat cupidatat non proident</h4><small><b>Admin</b>19.02.2020</small></div>
  <div class="article" style="left:465px;background:linear-gradient(180deg,#ededed 0%,#bdbdbd 30%,#7a7a7a 55%,#9a9a9a 70%,#2e2e2e 100%)" role="img" aria-label="Black and white living room interior"><h4>Excepteur sint occaecat cupidatat non proident</h4><small><b>Admin</b>19.02.2020</small></div>
  <div class="article" style="left:757px;background:linear-gradient(180deg,#e8e8e8 0%,#f4f4f4 30%,#b4b4b4 55%,#8c8c8c 75%,#6a6a6a 100%)" role="img" aria-label="Black and white kitchen interior"><h4>Excepteur sint occaecat cupidatat non proident</h4><small><b>Admin</b>19.02.2020</small></div>
</section>

<footer class="footer">
  <span class="copy">©Copyright information here</span>
  <span class="links">HOME | ABOUT | CONTACT</span>
  <div class="social" style="left:991px;top:29px"></div>
</footer>

</body>
</html>
```